Engineering Consultant Business Card

I'm starting a new business as a high-end engineering consultant in a niche field. I've attached the jpg for my logo plus the branding guideline document that I've been following. You can see my business website here: www.tarvikworks.com
I'd like a business card that has the logo on one side, then the other side has (in any order): Tarvik Works, Inc.
Dana Whitlock
President and Chief EMC Engineer
www.tarvikworks.com
dana@tarvikworks.com
Optional: motto "We will solve your EMC problems as early as possible—ideally before they even start."
I'm not planning on including a phone number
Target Market(s)
Businesses, especially makers of electronics hardware
Industry/Entity Type
Electrical engineering
Contact Information for Business Card
Company name, my name, website, email

```html
<!DOCTYPE html>
<html lang="en">
<head>
<meta charset="utf-8">
<title>Tarvik Works, Inc. — Business Card</title>
<link href="https://fonts.googleapis.com/css2?family=Lato:wght@400;700;900&display=swap" rel="stylesheet">
<style>
  :root{
    --backdrop:#1b1c1f;
    --brand-blue:#2b45a0;
    --deep-navy:#101a6b;
    --paper:#ffffff;
    --ink-light:#ffffff;
  }
  *{box-sizing:border-box;margin:0;padding:0}
  html,body{width:1200px;height:1122px;overflow:hidden;background:var(--backdrop)}
  body{font-family:"Lato",sans-serif;position:relative}
  .card{
    position:absolute;width:760px;height:434px;border-radius:26px;
    background:var(--brand-blue);overflow:hidden;
    box-shadow:0 18px 40px rgba(0,0,0,.55);
  }
  .card--back{left:220px;top:80px}
  .card--front{left:220px;top:600px}

  .back-mark{
    position:absolute;inset:0;display:flex;align-items:center;justify-content:center;
    font-weight:900;font-size:64px;letter-spacing:2px;color:var(--deep-navy);
  }

  .front-curve{position:absolute;inset:0;width:760px;height:434px}
  .front-mark{
    position:absolute;left:450px;top:215px;width:300px;text-align:center;
    font-weight:900;font-size:40px;letter-spacing:1px;color:var(--brand-blue);
  }
  .contact{position:absolute;left:48px;top:66px;color:var(--ink-light)}
  .contact__name{font-weight:900;font-size:28px;letter-spacing:.5px;text-transform:uppercase;line-height:1.1}
  .contact__title{font-weight:400;font-size:17px;margin-top:4px}
  .contact__company{font-weight:700;font-size:17px;margin-top:18px}
  .contact__list{list-style:none;margin-top:10px}
  .contact__item{display:flex;align-items:center;gap:10px;font-size:17px;line-height:1.6}
  .contact__icon{width:15px;height:15px;flex:none}
</style>
</head>
<body>

  <section class="card card--back" aria-label="Card back">
    <div class="back-mark">Tarvik Works</div>
  </section>

  <section class="card card--front" aria-label="Card front">
    <svg class="front-curve" viewBox="0 0 760 434" aria-hidden="true">
      <circle cx="660" cy="260" r="318" fill="none" stroke="#fff" stroke-width="3"/>
      <circle cx="660" cy="260" r="306" fill="none" stroke="#fff" stroke-width="3"/>
      <circle cx="660" cy="260" r="290" fill="#fff"/>
    </svg>

    <div class="front-mark">Tarvik Works</div>

    <div class="contact">
      <h1 class="contact__name">Dana Whitlock</h1>
      <p class="contact__title">President &amp; Chief EMC Engineer</p>
      <p class="contact__company">Tarvik Works, Inc.</p>
      <ul class="contact__list">
        <li class="contact__item">
          <svg class="contact__icon" viewBox="0 0 16 16"><rect x="1" y="3" width="14" height="10" fill="#fff"/><path d="M1 3l7 6 7-6" fill="none" stroke="#2b45a0" stroke-width="1.4"/></svg>
          dana@tarvikworks.com
        </li>
        <li class="contact__item">
          <svg class="contact__icon" viewBox="0 0 16 16"><circle cx="8" cy="8" r="6.5" fill="none" stroke="#fff" stroke-width="1.5"/><path d="M1.5 8h13M8 1.5c-3 3.5-3 9.5 0 13M8 1.5c3 3.5 3 9.5 0 13" fill="none" stroke="#fff" stroke-width="1.2"/></svg>
          tarvikworks.com
        </li>
      </ul>
    </div>
  </section>

</body>
</html>
```